5 Telephone Calling cards Design required

My Client is looking for 5 FIVE calling cards. The details are following:

1. All cards will be UK denomination.
2. One £5 face value card.
3. Four £1 face value cards.
4. All should be the universal designs.

The £5 card name is BRIZZLE PEAKS
The £1 card name ORB

You can use the 'ZEPPO GRID' or 'MINT KOVA' or 'PLUMO' cards as a samples to design the back side of all the cards.

Its an urgent project so please upload your entries as soon as possible.

some examples:

```html
<!DOCTYPE html>
<html lang="en">
<head>
<meta charset="utf-8">
<title>Brizzle Peaks £5 Prepaid Calling Card</title>
<link rel="stylesheet" href="https://fonts.googleapis.com/css2?family=Open+Sans:wght@300;400&family=Arimo:ital,wght@1,700&display=swap">
<style>
  :root {
    --backdrop: #3c3c3c;
    --panel-blue: rgba(100, 121, 160, 0.92);
    --photo-light: #f4f2ef;
    --photo-mid: #d9dde3;
    --photo-shade: #8f98aa;
    --band-orange: #f9a81a;
    --text-white: #ffffff;
  }
  html, body {
    margin: 0;
    padding: 0;
    width: 1200px;
    height: 900px;
    overflow: hidden;
    background: var(--backdrop);
  }
  .calling-card {
    position: absolute;
    left: 180px;
    top: 209px;
    width: 840px;
    height: 482px;
    overflow: hidden;
  }
  .photo-area {
    position: absolute;
    inset: 0;
    background:
      radial-gradient(ellipse at 72% 55%, var(--photo-shade) 0%, rgba(143,152,170,0) 45%),
      linear-gradient(100deg, var(--photo-mid) 0%, var(--photo-light) 60%, #e8e6e2 100%);
  }
  .blue-panel {
    position: absolute;
    left: 0;
    top: 0;
  }
  .brand-name {
    position: absolute;
    left: 25px;
    top: 28px;
    margin: 0;
    font-family: "Open Sans", sans-serif;
    font-weight: 300;
    font-size: 50px;
    line-height: 1;
    letter-spacing: -0.5px;
    color: var(--text-white);
    white-space: nowrap;
  }
  .face-value {
    position: absolute;
    left: 100px;
    top: 120px;
    margin: 0;
    font-family: "Open Sans", sans-serif;
    font-weight: 300;
    font-size: 190px;
    line-height: 1;
    color: var(--text-white);
  }
  .product-band {
    position: absolute;
    left: 0;
    bottom: 0;
    width: 840px;
    height: 73px;
    background: var(--band-orange);
  }
  .product-label {
    position: absolute;
    left: 59px;
    top: 12px;
    margin: 0;
    font-family: "Arimo", sans-serif;
    font-style: italic;
    font-weight: 700;
    font-size: 46px;
    line-height: 1;
    color: var(--text-white);
    white-space: nowrap;
  }
  .chevrons {
    position: absolute;
    left: 656px;
    top: 0;
  }
</style>
</head>
<body>
  <div class="calling-card">
    <div class="photo-area" role="img" aria-label="Photo of a smiling young woman in a checked shirt lying on a bed, talking on a mobile phone in a bright room"></div>

    <svg class="blue-panel" width="840" height="482" viewBox="0 0 840 482" aria-hidden="true">
      <path d="M0 0 H507 Q 478 250 413 409 H0 Z" fill="var(--panel-blue)"/>
    </svg>

    <h1 class="brand-name">BRIZZLE PEAKS</h1>
    <p class="face-value">£5</p>

    <div class="product-band">
      <p class="product-label">Prepaid Calling Card</p>
      <svg class="chevrons" width="130" height="73" viewBox="0 0 130 73" aria-hidden="true">
        <path d="M0 0 H22 L44 36.5 L22 73 H0 L22 36.5 Z" fill="var(--text-white)"/>
        <path d="M40 0 H62 L84 36.5 L62 73 H40 L62 36.5 Z" fill="var(--text-white)"/>
        <path d="M80 0 H102 L124 36.5 L102 73 H80 L102 36.5 Z" fill="var(--text-white)"/>
      </svg>
    </div>
  </div>
</body>
</html>
```